Natural Light/Organic/Documentary Photography Business

I like a simple, approachable, feminine, earthy/organic feel. Earth/neutral tones, nothing too loud or obnoxious. I like the watercolor look. I don't want anything too trendy or something I'll get tired of after a couple months. As far as colors, I am much more a fan of cream/taupe/blue/green...not a fan of pink or purple at all.

Target Market(s)

Weddings & Families

Industry/Entity Type

Wedding Photography

Contact Information for Business Card

website, email, phone number

Font styles to use
Other font styles liked:
• Horizontes, Gotham

Colors

Designer to choose colors to be used in the design.

Requirements
Must have
• Website: www.meliskaverholt.com
• Phone: 482.319.6047
• Email: tessa@meliskaverholt.com
Nice to have
• I like the watercolor look but its not necessary. I like simple/earthy tones. Nothing too loud or distracting. Simple & feminine without being too girly. I like an approachable/soft feel.
• Instagram: www.instagram.com/meliskaverholtphotography/
Should not have
• NO loud colors or design or pattern. I do not want a photo of a camera or lens or anything cheesy like that.

```html
<!DOCTYPE html>
<html lang="en">
<head>
<meta charset="utf-8">
<title>Meliska Verholt Photography — Business Card</title>
<link rel="stylesheet" href="https://fonts.googleapis.com/css2?family=Montserrat:wght@400;500&family=Sacramento&display=swap">
<style>
  :root {
    --page: #ffffff;
    --card: #ffffff;
    --ink: #8a7e76;
    --ink-strong: #7a6e66;
    --frame: #a89d95;
    --taupe: #bdb2a9;
    --taupe-light: #d9d1ca;
    --mint: #96c9b3;
    --teal: #5f8985;
    --sky: #a9d6e0;
    --mist: #f4f9fa;
  }
  * { margin: 0; padding: 0; box-sizing: border-box; }
  html, body {
    width: 1200px;
    height: 867px;
    overflow: hidden;
    background: var(--page);
  }
  .card {
    position: absolute;
    left: 100px;
    top: 128px;
    width: 1000px;
    height: 610px;
    background: var(--card);
  }
  .wash {
    position: absolute;
    left: 72px;
    top: 64px;
    width: 855px;
    height: 481px;
    background:
      linear-gradient(180deg, rgba(255,255,255,0) 55%, rgba(255,255,255,0.55) 100%),
      linear-gradient(90deg,
        var(--taupe) 0%,
        var(--taupe) 30%,
        var(--taupe-light) 38%,
        var(--mint) 46%,
        var(--teal) 60%,
        var(--mint) 70%,
        var(--sky) 82%,
        var(--mist) 100%);
  }
  .panel {
    position: absolute;
    left: 184px;
    top: 163px;
    width: 633px;
    height: 287px;
    background: var(--card);
    border: 1px solid var(--frame);
    text-align: center;
    font-family: "Montserrat", sans-serif;
    color: var(--ink);
  }
  .brand-name {
    margin-top: 36px;
    font-family: "Sacramento", cursive;
    font-weight: 400;
    font-size: 76px;
    line-height: 1;
    color: var(--ink);
  }
  .brand-tagline {
    margin-top: 0;
    font-size: 11px;
    letter-spacing: 0.55em;
    padding-left: 0.55em;
    font-weight: 400;
    color: var(--ink);
  }
  .contact {
    list-style: none;
    margin-top: 44px;
    font-size: 13px;
    line-height: 24.5px;
    color: var(--ink);
  }
  .contact-label {
    font-weight: 500;
    color: var(--ink-strong);
  }
  .contact-sep { margin: 0 4px; }
  .contact-dot { margin: 0 10px; }
</style>
</head>
<body>
  <section class="card">
    <div class="wash" role="img" aria-label="Soft watercolour wash in taupe, mint, teal and pale blue"></div>
    <div class="panel">
      <h1 class="brand-name">Meliska Verholt</h1>
      <p class="brand-tagline">PHOTOGRAPHY</p>
      <ul class="contact">
        <li>
          <span class="contact-label">Website</span><span class="contact-sep">|</span>www.meliskaverholt.com<span class="contact-dot">·</span><span class="contact-label">Phone</span><span class="contact-sep">|</span>482 319 6047
        </li>
        <li>
          <span class="contact-label">Email</span><span class="contact-sep">|</span>tessa@meliskaverholt.com
        </li>
        <li>
          <span class="contact-label">Instagram</span><span class="contact-sep">|</span>@meliskaverholtphotography
        </li>
      </ul>
    </div>
  </section>
</body>
</html>
```